Kit Darvell - health and fitness coach who needs a web page. simple and effective

I am a online health and fitness coach who runs a 10 week challenge 4 times a year. I am wanting, a menu with a bit about me, a place where people can buy the programme, testimonies, memberships, photos, and recipes.
I am wanting it to look modern, professional and simple.
The website is how potential clients can check out the memberships for the programme, photos of myself and and my family to show members that I am a confident, educated, independent and healthy woman. Who is very passionate about making a difference in people lives to become a better version of themselves.
My training philosophy is simple, Commitment to training, Consistently working hard and training equals Change! Change is physical changes to the body!!

Target Market(s)

Woman 25-44 years

Industry/Entity Type

Health And Wellness

Coding

Coded - Design and coding required

Number of Pages Required

5+ page

Font styles to use
Sans Serif

Colors
fbed22
e667a6
ffffff

Requirements
Must have
• I like the style of "plain tile" website design.
• On the menu bar I want 9 different tabs/options to click on, these are named:
• BLOG
• ABOUT
• TRAINING PROGRAMS
• HEALTHY FOOD
• SUBSCRIBE
• TESTIMONIALS
• CHATWALL
• SNAPLOOMER
• VID REEL
Nice to have
• logo at the top (attached under file 2)
• Easy for myself to add information once website design is completed.
• lots of white space, white a bright yellow (same as logo) or pink
Should not have
• clutter

```html
<!DOCTYPE html>
<html lang="en">
<head>
<meta charset="utf-8">
<title>Kit Darvell – Healthy Fitness Lifestyle</title>
<link href="https://fonts.googleapis.com/css2?family=Alegreya+Sans:wght@500;700;800&family=Arimo:wght@400;700&family=Gochi+Hand&display=swap" rel="stylesheet">
<style>
:root{
  --yellow:#fbed22;
  --pink:#e667a6;
  --white:#ffffff;
  --ink:#111111;
  --body:#555555;
  --grey-band:#efefef;
  --dark:#1b1b1b;
  --footer:#262626;
}
*{margin:0;padding:0;box-sizing:border-box}
html,body{width:1200px;height:3766px;overflow:hidden}
body{position:relative;background:var(--white);font-family:'Arimo',Arial,sans-serif;color:var(--ink)}
.abs{position:absolute}

/* header */
.site-header{left:0;top:0;width:1200px;height:138px;background:var(--white)}
.brand{left:78px;top:22px;display:flex;align-items:center;gap:14px}
.brand-mark{width:44px;height:44px;background:var(--yellow)}
.brand-name{font-family:'Alegreya Sans',sans-serif;font-weight:700;font-size:30px;color:var(--yellow);line-height:1;letter-spacing:1px}
.brand-tag{left:136px;top:72px;font-family:'Alegreya Sans',sans-serif;font-weight:700;font-size:11px;color:var(--ink)}
.contact{top:34px;display:flex;gap:12px;align-items:center}
.contact-icon{width:36px;height:28px;background:var(--yellow);display:flex;align-items:center;justify-content:center}
.contact-label{font-size:14px;color:#777;line-height:1.2}
.contact-value{font-size:18px;color:var(--ink);line-height:1.2}
.header-social{top:42px;right:78px;display:flex;gap:16px}
.header-social span{width:16px;height:16px;border-radius:50%;background:var(--ink)}

.main-nav{left:78px;top:110px;width:1044px;height:60px;background:var(--yellow);display:flex;justify-content:space-around;align-items:center;z-index:2}
.main-nav a{font-size:15px;color:var(--ink);text-decoration:none}

/* hero */
.hero{left:0;top:138px;width:1200px;height:622px;background:linear-gradient(180deg,#3c4650 0%,#6a7a86 45%,#7e8b90 62%,#5d574c 80%,#4a4136 100%)}
.hero-tagline{left:78px;top:306px;font-family:'Gochi Hand',cursive;font-size:40px;color:var(--yellow)}
.hero-title{left:78px;top:382px;font-family:'Alegreya Sans',sans-serif;font-weight:800;font-size:52px;line-height:1.32;color:var(--white)}
.btn{background:var(--yellow);color:var(--ink);font-family:'Alegreya Sans',sans-serif;font-weight:800;font-size:16px;display:flex;align-items:center;justify-content:center;text-transform:uppercase}
.hero-btn{left:78px;top:540px;width:144px;height:50px}
.dots{left:560px;top:700px;display:flex;gap:12px;align-items:center}
.dots span{width:16px;height:16px;border-radius:50%;background:var(--white)}
.dots span.active{width:22px;height:22px;border:4px solid #bbb}

/* section heads */
.section-title{left:0;width:1200px;text-align:center;font-family:'Alegreya Sans',sans-serif;font-weight:800;font-size:50px;line-height:1}
.section-title span{position:relative}
.section-title span::after{content:"";position:absolute;left:calc(100% + 28px);top:55%;width:64px;height:4px;background:var(--yellow)}
.section-text{left:250px;width:700px;text-align:center;font-size:14px;line-height:26px;color:var(--body)}

.photo{position:absolute}

/* training */
.training{left:0;top:1418px;width:1200px;height:730px;background:linear-gradient(180deg,#2a2a2a,#141414 60%,#1c1c1c)}

/* testimonials */
.testimonials{left:0;top:2753px;width:1200px;height:490px;background:var(--grey-band)}
.quote-card{width:500px;height:155px;background:var(--white);border-top:3px solid var(--yellow);padding:30px 30px 0 76px;font-size:15px;line-height:27px;color:var(--body)}
.quote-mark{position:absolute;left:26px;top:22px;font-family:'Alegreya Sans',sans-serif;font-weight:800;font-size:56px;line-height:1;color:var(--yellow)}
.quote-card::after{content:"";position:absolute;left:70px;bottom:-22px;border-left:22px solid transparent;border-right:22px solid transparent;border-top:22px solid var(--white)}
.client{display:flex;align-items:center;gap:10px;font-size:15px;color:#333}
.avatar{width:86px;height:86px;border-radius:50%;border:4px solid var(--yellow);background:linear-gradient(160deg,#8a6a55,#d9b9a0)}

/* subscribe */
.field{height:50px;border:2px solid #333;background:var(--white);font-size:15px;color:#555;display:flex;align-items:center;padding-left:12px}

/* footer */
.site-footer{left:0;top:3544px;width:1200px;height:222px;background:linear-gradient(180deg,#2b2b2b,#1c1c1c)}
.footer-nav{left:0;top:3588px;width:1200px;display:flex;justify-content:center;font-size:15px;color:var(--white)}
.footer-nav a{color:var(--white);text-decoration:none;padding:0 14px;border-right:1px solid var(--white);line-height:16px}
.footer-nav a:last-child{border-right:none}
.footer-social{left:0;top:3638px;width:1200px;display:flex;justify-content:center;gap:18px}
.footer-social span{width:38px;height:38px;border-radius:50%;background:var(--white)}
.footer-rule{left:78px;top:3700px;width:1044px;height:1px;background:#777}
.copyright{left:0;top:3724px;width:1200px;text-align:center;font-size:15px;color:var(--white)}
</style>
</head>
<body>

<header class="site-header abs">
  <div class="brand abs"><div class="brand-mark"></div><div class="brand-name">KIT DARVELL</div></div>
  <div class="brand-tag abs">Fitness Health Lifestyle</div>

  <div class="contact abs" style="left:470px">
    <div class="contact-icon">
      <svg width="18" height="18" viewBox="0 0 24 24"><path d="M6.6 10.8c1.4 2.8 3.8 5.1 6.6 6.6l2.2-2.2c.3-.3.7-.4 1-.2 1.1.4 2.300.6 3.600.6.6 0 1 .4 1 1V20c0 .6-.4 1-1 1C10.6 21 3 13.4 3 4c0-.6.4-1 1-1h3.5c.6 0 1 .4 1 1 0 1.3.2 2.5.6 3.6.1.3 0 .7-.2 1z" fill="#111"/></svg>
    </div>
    <div><div class="contact-label">Call Us</div><div class="contact-value">555 014 2290</div></div>
  </div>
  <div class="contact abs" style="left:670px">
    <div class="contact-icon">
      <svg width="20" height="16" viewBox="0 0 20 16"><rect x="1" y="1" width="18" height="14" fill="none" stroke="#111" stroke-width="2"/><path d="M1 1l9 7 9-7" fill="none" stroke="#111" stroke-width="2"/></svg>
    </div>
    <div><div class="contact-label">E-mail</div><div class="contact-value">hello@kitdarvell.com</div></div>
  </div>
  <div class="header-social abs"><span></span><span></span><span></span></div>
</header>

<nav class="main-nav abs">
  <a href="#">About</a><a href="#">Blog</a><a href="#">Training Programs</a><a href="#">Healthy Food</a><a href="#">Subscribe</a><a href="#">Testimonials</a><a href="#">Chatwall</a><a href="#">Snaploomer</a><a href="#">Vid Reel</a>
</nav>

<section class="hero abs" role="img" aria-label="Coach doing a handstand on a beach at dusk"></section>
<div class="hero-tagline abs">Inspiring you to live a healthier lifestyle.</div>
<h1 class="hero-title abs">Hi, I'm KIT DARVELL<br>Your Health Advisor.</h1>
<div class="btn hero-btn abs">Contact Us</div>
<div class="dots abs"><span></span><span class="active"></span><span></span></div>

<h2 class="section-title abs" style="top:828px"><span>About Us</span></h2>
<p class="section-text abs" style="top:902px">Kit Darvell is Coach Kit. A health and fitness coach since 2008 after completing a Bachelor of Recreation and Sports at Harrowfield University. She has also obtained other qualifications of National Strength and Conditioning Coach Level 1</p>
<div class="btn abs" style="left:505px;top:1012px;width:146px;height:50px">Learn More</div>
<div class="photo" role="img" aria-label="Salad with boiled eggs and bacon" style="left:78px;top:1094px;width:339px;height:261px;background:linear-gradient(135deg,#6b8c3a,#c9573c 50%,#efe3c8)"></div>
<div class="photo" role="img" aria-label="Coach lying on grass giving thumbs up" style="left:430px;top:1094px;width:338px;height:261px;background:linear-gradient(180deg,#9bb06a,#5f8a36)"></div>
<div class="photo" role="img" aria-label="Group of runners after a race" style="left:783px;top:1094px;width:339px;height:261px;background:linear-gradient(180deg,#5b6d8a,#2a2a32 60%,#7a2630)"></div>

<section class="training abs" role="img" aria-label="Dim gym interior background"></section>
<h2 class="section-title abs" style="top:1483px;color:var(--white)"><span>Training Programs</span></h2>
<p class="section-text abs" style="top:1560px;color:var(--white)">Kit's passion and motivation for fitness is infectious, attracting people worldwide who complete her online fitness programs.</p>
<div class="btn abs" style="left:527px;top:1640px;width:146px;height:50px">Learn More</div>
<div class="photo" role="img" aria-label="Man sprinting on a country road" style="left:78px;top:1720px;width:509px;height:366px;background:linear-gradient(180deg,#c9ccc8,#6e7b52 40%,#6b6b68)"></div>
<div class="photo" role="img" aria-label="Coach training with a kettlebell in a garage gym" style="left:610px;top:1720px;width:512px;height:366px;background:linear-gradient(180deg,#a9a9a6,#7c7a74 60%,#2e2e2c)"></div>

<h2 class="section-title abs" style="top:2212px"><span>Healthy Food</span></h2>
<div class="photo" role="img" aria-label="Berry smoothie" style="left:78px;top:2294px;width:339px;height:191px;background:linear-gradient(180deg,#e87aa0,#f2a4b6)"></div>
<div class="photo" role="img" aria-label="Hummus dip with carrot sticks" style="left:430px;top:2294px;width:338px;height:397px;background:linear-gradient(180deg,#d8d2c4,#e8772a 60%,#c8521a)"></div>
<div class="photo" role="img" aria-label="Yoghurt with nuts and dates" style="left:783px;top:2294px;width:339px;height:191px;background:linear-gradient(180deg,#8a6a52,#ece6dc)"></div>
<div class="photo" role="img" aria-label="Cranberry oat muffins" style="left:78px;top:2500px;width:339px;height:191px;background:linear-gradient(135deg,#b98d55,#e0c18e)"></div>
<div class="photo" role="img" aria-label="Chocolate avocado smoothie" style="left:783px;top:2500px;width:339px;height:191px;background:linear-gradient(135deg,#6b4a36,#b4906e 60%,#3f5a24)"></div>

<section class="testimonials abs"></section>
<h2 class="section-title abs" style="top:2816px"><span>Testimonial</span></h2>
<div class="quote-card abs" style="left:78px;top:2902px"><span class="quote-mark">“</span>Lorem Ipsum is simply dummy text of the printing and typesetting industry. Lorem Ipsum has been the industry's standard dummy text ever since the 1500s, when an unknown printer took</div>
<div class="quote-card abs" style="left:622px;top:2902px"><span class="quote-mark">“</span>Lorem Ipsum is simply dummy text of the printing and typesetting industry. Lorem Ipsum has been the industry's standard dummy text ever since the 1500s, when an unknown printer took</div>
<div class="client abs" style="left:128px;top:3094px"><div class="avatar" role="img" aria-label="Client portrait"></div>- CLIENT NAME</div>
<div class="client abs" style="left:672px;top:3094px"><div class="avatar" role="img" aria-label="Client portrait"></div>- CLIENT NAME</div>

<h2 class="section-title abs" style="top:3308px"><span>Subscribe Now!</span></h2>
<p class="section-text abs" style="top:3376px">Want to be the first in the know for Kit Darvell's announcements? Subscribe here!</p>
<div class="field abs" style="left:268px;top:3431px;width:248px">Name*</div>
<div class="field abs" style="left:527px;top:3431px;width:250px">E-mail*</div>
<div class="btn abs" style="left:788px;top:3431px;width:143px;height:50px">Subscribe</div>

<footer class="site-footer abs" role="img" aria-label="Dark gym backdrop"></footer>
<nav class="footer-nav abs">
  <a href="#">About</a><a href="#">Blog</a><a href="#">Training Programs</a><a href="#">Healthy Food</a><a href="#">Subscribe</a><a href="#">Testimonial</a><a href="#">Chatwall</a><a href="#">Snaploomer</a><a href="#">Vid Reel</a>
</nav>
<div class="footer-social abs"><span></span><span></span><span></span></div>
<div class="footer-rule abs"></div>
<div class="copyright abs">© KIT DARVELL HEALTHY FITNESS LIFESTYLE - 2018. All Rights Reserved.</div>

</body>
</html>
```